Step and Repeat Backdrop for wedding reception photo booth

Would like to have a Step and Repeat Backdrop (8 foot high by 10 foot wide) that incorporates the wedding logo (attached) and the names Clara and Bruno. Background should be white, and wedding colors are burgundy and gold. Show me creativity :-) I have included some random samples.

```html
<!DOCTYPE html>
<html lang="en">
<head>
<meta charset="utf-8">
<title>Clara &amp; Bruno — Step and Repeat Backdrop</title>
<link rel="stylesheet" href="https://fonts.googleapis.com/css2?family=Pinyon+Script&family=Cinzel:wght@600&display=swap">
<style>
  :root {
    --page-bg: #f2f1f1;
    --board-white: #ffffff;
    --gold-deep: #a07f45;
    --gold-light: #c9ab69;
    --gold-ink: #a88548;
    --name-ink: #a87a3e;
    --name-edge: #7a4f24;
    --tile: 118px;
  }
  * { box-sizing: border-box; margin: 0; padding: 0; }
  html, body {
    width: 1200px; height: 1000px; overflow: hidden;
    background: var(--page-bg);
  }
  .backdrop {
    position: absolute; left: 53px; top: 71px;
    width: 1094px; height: 858px;
    background: var(--board-white);
    border: 1px solid #8a8a8a;
    box-shadow: 0 6px 24px rgba(0,0,0,0.18);
    padding: 15px;
  }
  .backdrop__grid {
    display: grid;
    grid-template-columns: repeat(9, var(--tile));
    grid-template-rows: repeat(7, var(--tile));
  }
  .tile {
    display: flex; align-items: center; justify-content: center;
  }
  .tile--names {
    background: linear-gradient(90deg, var(--gold-deep), var(--gold-light) 60%, var(--gold-deep));
    color: #fff;
    font-family: "Pinyon Script", cursive;
    flex-direction: column; line-height: 0.9;
  }
  .tile--names .first { font-size: 30px; align-self: flex-start; margin-left: 12px; }
  .tile--names .and { font-size: 20px; margin-right: 30px; }
  .tile--names .second { font-size: 30px; align-self: flex-end; margin-right: 14px; }
  .tile--monogram {
    font-family: "Cinzel", serif; font-weight: 600;
    font-size: 26px; color: var(--gold-ink); letter-spacing: -1px;
  }
  .feature-names {
    position: absolute; left: 0; top: 0; width: 100%; height: 100%;
    pointer-events: none;
    font-family: "Pinyon Script", cursive;
    font-weight: 400;
    color: var(--name-ink);
    text-shadow: 0 1px 0 var(--name-edge);
  }
  .feature-names span { position: absolute; line-height: 1; white-space: nowrap; }
  .feature-names .first  { font-size: 104px; left: 385px; top: 278px; }
  .feature-names .amp    { font-size: 84px;  left: 345px; top: 385px; }
  .feature-names .second { font-size: 104px; left: 425px; top: 400px; }
  .stand { position: absolute; bottom: -5px; width: 56px; height: 5px; background: #8a8a8a; border-radius: 3px; }
  .stand--left { left: 40px; } .stand--right { right: 46px; }
</style>
</head>
<body>
<div class="backdrop">
  <div class="backdrop__grid">
    <div class="tile tile--monogram">C&amp;B</div><div class="tile tile--names"><span class="first">Clara</span><span class="and">and</span><span class="second">Bruno</span></div><div class="tile tile--monogram">C&amp;B</div><div class="tile tile--names"><span class="first">Clara</span><span class="and">and</span><span class="second">Bruno</span></div><div class="tile tile--monogram">C&amp;B</div><div class="tile tile--names"><span class="first">Clara</span><span class="and">and</span><span class="second">Bruno</span></div><div class="tile tile--monogram">C&amp;B</div><div class="tile tile--names"><span class="first">Clara</span><span class="and">and</span><span class="second">Bruno</span></div><div class="tile tile--monogram">C&amp;B</div>

    <div class="tile tile--names"><span class="first">Clara</span><span class="and">and</span><span class="second">Bruno</span></div><div class="tile tile--monogram">C&amp;B</div><div class="tile tile--names"><span class="first">Clara</span><span class="and">and</span><span class="second">Bruno</span></div><div class="tile tile--monogram">C&amp;B</div><div class="tile tile--names"><span class="first">Clara</span><span class="and">and</span><span class="second">Bruno</span></div><div class="tile tile--monogram">C&amp;B</div><div class="tile tile--names"><span class="first">Clara</span><span class="and">and</span><span class="second">Bruno</span></div><div class="tile tile--monogram">C&amp;B</div><div class="tile tile--names"><span class="first">Clara</span><span class="and">and</span><span class="second">Bruno</span></div>

    <div class="tile tile--monogram">C&amp;B</div><div class="tile tile--names"><span class="first">Clara</span><span class="and">and</span><span class="second">Bruno</span></div><div class="tile tile--monogram">C&amp;B</div><div class="tile"></div><div class="tile"></div><div class="tile"></div><div class="tile tile--monogram">C&amp;B</div><div class="tile tile--names"><span class="first">Clara</span><span class="and">and</span><span class="second">Bruno</span></div><div class="tile tile--monogram">C&amp;B</div>

    <div class="tile tile--names"><span class="first">Clara</span><span class="and">and</span><span class="second">Bruno</span></div><div class="tile tile--monogram">C&amp;B</div><div class="tile"></div><div class="tile"></div><div class="tile"></div><div class="tile"></div><div class="tile"></div><div class="tile tile--monogram">C&amp;B</div><div class="tile tile--names"><span class="first">Clara</span><span class="and">and</span><span class="second">Bruno</span></div>

    <div class="tile tile--monogram">C&amp;B</div><div class="tile tile--names"><span class="first">Clara</span><span class="and">and</span><span class="second">Bruno</span></div><div class="tile tile--monogram">C&amp;B</div><div class="tile"></div><div class="tile"></div><div class="tile"></div><div class="tile tile--monogram">C&amp;B</div><div class="tile tile--names"><span class="first">Clara</span><span class="and">and</span><span class="second">Bruno</span></div><div class="tile tile--monogram">C&amp;B</div>

    <div class="tile tile--names"><span class="first">Clara</span><span class="and">and</span><span class="second">Bruno</span></div><div class="tile tile--monogram">C&amp;B</div><div class="tile tile--names"><span class="first">Clara</span><span class="and">and</span><span class="second">Bruno</span></div><div class="tile tile--monogram">C&amp;B</div><div class="tile tile--names"><span class="first">Clara</span><span class="and">and</span><span class="second">Bruno</span></div><div class="tile tile--monogram">C&amp;B</div><div class="tile tile--names"><span class="first">Clara</span><span class="and">and</span><span class="second">Bruno</span></div><div class="tile tile--monogram">C&amp;B</div><div class="tile tile--names"><span class="first">Clara</span><span class="and">and</span><span class="second">Bruno</span></div>

    <div class="tile tile--monogram">C&amp;B</div><div class="tile tile--names"><span class="first">Clara</span><span class="and">and</span><span class="second">Bruno</span></div><div class="tile tile--monogram">C&amp;B</div><div class="tile tile--names"><span class="first">Clara</span><span class="and">and</span><span class="second">Bruno</span></div><div class="tile tile--monogram">C&amp;B</div><div class="tile tile--names"><span class="first">Clara</span><span class="and">and</span><span class="second">Bruno</span></div><div class="tile tile--monogram">C&amp;B</div><div class="tile tile--names"><span class="first">Clara</span><span class="and">and</span><span class="second">Bruno</span></div><div class="tile tile--monogram">C&amp;B</div>
  </div>
  <h1 class="feature-names"><span class="first">Clara</span><span class="amp">&amp;</span><span class="second">Bruno</span></h1>
  <div class="stand stand--left"></div>
  <div class="stand stand--right"></div>
</div>
</body>
</html>
```